Bref créative
Sun Path & Oak Hill
Business Cards & Stationary
Use same font as used in my logo
marla teswick
director of operations
p o box 87
gravette, ar 72915
spoh@postvale.com
501(c)3

```html
<!DOCTYPE html>
<html lang="en">
<head>
<meta charset="utf-8">
<title>Sun Path &amp; Oak Hill — Stationery</title>
<link href="https://fonts.googleapis.com/css2?family=Dancing+Script:wght@500&family=Questrial&display=swap" rel="stylesheet">
<style>
  :root{
    --paper:#ffffff;
    --edge:#9a9a9a;
    --fold:#c4c4c4;
    --ink:#3a3a3a;
    --pink:#e8739f;
    --blush:#f6bfd1;
  }
  *{box-sizing:border-box;margin:0;padding:0}
  html,body{width:1200px;height:1101px;overflow:hidden;background:var(--paper)}
  body{position:relative;font-family:"Questrial",sans-serif;color:var(--ink)}

  .sheet{position:absolute;background:var(--paper);border:1.5px solid var(--edge)}
  .letterhead{left:24px;top:54px;width:885px;height:1011px}
  .business-card{left:915px;top:54px;width:270px;height:156px;overflow:hidden}

  .brand{position:absolute;display:flex;flex-direction:column;align-items:center}
  .brand-row{display:flex;align-items:center;gap:12px}
  .brand-dot{border-radius:50%;background:var(--blush);flex:none}
  .brand-name{font-family:"Dancing Script",cursive;font-weight:500;color:var(--ink);white-space:nowrap;line-height:1}
  .brand-tagline{color:var(--pink);letter-spacing:.28em;text-transform:uppercase;white-space:nowrap}

  .letterhead .brand{left:0;right:0;top:48px}
  .letterhead .brand-dot{width:56px;height:56px}
  .letterhead .brand-name{font-size:44px}
  .letterhead .brand-tagline{font-size:14px;margin-top:8px}

  .letterhead-footer{position:absolute;left:0;right:0;bottom:22px;text-align:center;font-size:13px;white-space:nowrap}
  .letterhead-footer .sep{color:var(--pink)}

  .business-card .brand{left:8px;top:36px;width:134px}
  .business-card .brand-row{gap:4px}
  .business-card .brand-dot{width:14px;height:14px}
  .business-card .brand-name{font-size:13px}
  .business-card .brand-tagline{font-size:6px;margin-top:4px;letter-spacing:.2em}
  .card-details{position:absolute;left:152px;top:26px;font-size:8.5px;line-height:1.45;white-space:nowrap}
  .card-name{color:var(--pink);font-size:12px;font-weight:700;line-height:1.2}
  .card-title{font-size:8px;margin-bottom:10px}

  .envelope{position:absolute;left:525px;top:420px;width:660px;height:555px}
  .envelope svg{position:absolute;inset:0}
  .envelope .brand{left:0;right:0;top:270px}
  .envelope .brand-dot{width:46px;height:46px}
  .envelope .brand-name{font-size:36px}
  .envelope .brand-tagline{font-size:12px;margin-top:7px}
  .return-address{position:absolute;left:0;right:0;top:487px;text-align:center;font-size:12px}
</style>
</head>
<body>

<section class="sheet letterhead" aria-label="Letterhead">
  <div class="brand">
    <div class="brand-row">
      <span class="brand-dot"></span>
      <span class="brand-name">Sun Path &amp; Oak Hill</span>
    </div>
    <div class="brand-tagline">walk together</div>
  </div>
  <p class="letterhead-footer">
    PO box 87 millbrook, ks 66915 <span class="sep">/</span> P: 620 555 0142 <span class="sep">/</span> E: spoh@postvale.com <span class="sep">/</span> L: 501c3
  </p>
</section>

<section class="sheet business-card" aria-label="Business card">
  <div class="brand">
    <div class="brand-row">
      <span class="brand-dot"></span>
      <span class="brand-name">Sun Path &amp; Oak Hill</span>
    </div>
    <div class="brand-tagline">walk together</div>
  </div>
  <div class="card-details">
    <p class="card-name">marla teswick</p>
    <p class="card-title">director of operations</p>
    <p>p o box 87</p>
    <p>millbrook, ks 66915</p>
    <p>spoh@postvale.com</p>
    <p>501c3</p>
  </div>
</section>

<section class="envelope" aria-label="Envelope">
  <svg width="660" height="555" viewBox="0 0 660 555">
    <polygon points="1,129 44,1 616,1 659,129" fill="#ffffff" stroke="#9a9a9a" stroke-width="1.5"/>
    <polyline points="1,129 330,40 659,129" fill="none" stroke="#c4c4c4" stroke-width="1"/>
    <rect x="1" y="129" width="658" height="425" fill="#ffffff" stroke="#9a9a9a" stroke-width="1.5"/>
    <circle cx="330" cy="36" r="16" fill="#f6bfd1"/>
  </svg>
  <div class="brand">
    <div class="brand-row">
      <span class="brand-dot"></span>
      <span class="brand-name">Sun Path &amp; Oak Hill</span>
    </div>
    <div class="brand-tagline">walk together</div>
  </div>
  <p class="return-address">p o box 87 millbrook, ks 66915</p>
</section>

</body>
</html>
```